Profesional personal website needs design and business card

I need a business card with my professional name as a logo "Marlo Vitality" for my business. I am a Wellness Coach, consultant and trainer. So it should be professional, wellness oriented and modern.

Target Market(s)

Private clients, governments, corporations. Luxury and high market.

Industry/Entity Type

Health And Wellness

Contact Information for Business Card

Marlo Vitality should be the logo

Colors

Designer to choose colors to be used in the design.

Requirements
Must have
• Marlo Vitality
• Name: Tomás Arribal
• Wellness Coach, Consultant & Trainer.
• Website: www.marlovitality.example
• Phone:
• Spain (+34) 612 480 397
• (USA) +1 (555) 318 2046
Nice to have
• The most important is the design of "Marlo Vitality", as this is going to be my personal brand logo. It should be professional, wellness, high end and actual.
Should not have
• no golds, no baroque style..

```html
<!DOCTYPE html>
<html lang="en">
<head>
<meta charset="utf-8">
<title>Marlo Vitality — Business Card</title>
<link rel="stylesheet" href="https://fonts.googleapis.com/css2?family=Open+Sans:wght@600;700&family=Comfortaa:wght@400;500&display=swap">
<style>
  :root {
    --backdrop: #0e8793;
    --brand-blue: #1f6db0;
    --brand-green: #3bb13f;
    --blue-mid: #2a79a6;
    --paper: #efefef;
    --ink: #2b2b2b;
    --ink-soft: #3a3a3a;
    --bar-dark: #3d4450;
  }
  * { box-sizing: border-box; margin: 0; padding: 0; }
  html, body {
    width: 1200px; height: 900px; overflow: hidden;
    background: var(--backdrop);
  }
  .canvas { position: relative; width: 1200px; height: 900px; }
  .card {
    position: absolute; left: 330px;
    width: 540px; height: 349px; overflow: hidden;
  }
  .card--front {
    top: 75px;
    background:
      radial-gradient(ellipse 70% 75% at 100% 100%, var(--brand-green) 0%, rgba(59,177,63,0.55) 35%, rgba(42,121,166,0) 75%),
      linear-gradient(160deg, var(--brand-blue) 0%, var(--blue-mid) 45%, var(--brand-blue) 100%);
    display: flex; align-items: center; justify-content: center;
  }
  .front-wordmark {
    font-family: "Open Sans", sans-serif; font-weight: 700;
    font-size: 62px; color: #f2f2f2; letter-spacing: 0.5px;
  }
  .card--back { top: 476px; background: var(--paper); }
  .brand-block { position: absolute; left: 18px; top: 50px; }
  .back-wordmark {
    font-family: "Open Sans", sans-serif; font-weight: 700;
    font-size: 37px; line-height: 38px; color: var(--brand-blue); letter-spacing: -0.3px;
  }
  .role {
    font-family: "Open Sans", sans-serif; font-weight: 600;
    font-size: 13.5px; line-height: 16px; color: var(--ink);
  }
  .accent-bar {
    position: absolute; left: 18px; top: 108px;
    width: 146px; height: 6px; border-radius: 3px;
    background: linear-gradient(90deg, var(--bar-dark), var(--brand-blue));
  }
  .person-name {
    position: absolute; left: 18px; top: 124px;
    font-family: "Open Sans", sans-serif; font-weight: 600;
    font-size: 15px; line-height: 18px; color: var(--ink);
  }
  .contact-icon { position: absolute; left: 22px; fill: var(--brand-blue); }
  .contact-icon--phone { top: 163px; width: 48px; height: 48px; }
  .contact-icon--web { top: 240px; width: 45px; height: 45px; }
  .phones {
    position: absolute; left: 88px; top: 159px;
    font-family: "Comfortaa", sans-serif; font-weight: 500;
    font-size: 21px; line-height: 29px; letter-spacing: 3px; color: var(--ink-soft);
  }
  .website {
    position: absolute; left: 91px; top: 251px;
    font-family: "Comfortaa", sans-serif; font-weight: 500;
    font-size: 19px; letter-spacing: 3.8px; color: var(--ink-soft);
  }
  .footer-band {
    position: absolute; left: 0; bottom: 0;
    width: 100%; height: 39px; background: var(--brand-blue);
  }
</style>
</head>
<body>
<main class="canvas">
  <section class="card card--front">
    <span class="front-wordmark">Marlo Vitality</span>
  </section>

  <section class="card card--back">
    <div class="brand-block">
      <div class="back-wordmark">Marlo Vitality</div>
      <div class="role">Wellness Coach, Consultant &amp; Trainer</div>
    </div>
    <div class="accent-bar"></div>
    <div class="person-name">Tomás Arribal</div>

    <svg class="contact-icon contact-icon--phone" viewBox="0 0 48 48" aria-hidden="true">
      <path d="M2 12c0-5 10-8 22-8s22 3 22 8v3h-9v-4c-4-1-8-1.5-13-1.5S15 10 11 11v4H2z"/>
      <rect x="15" y="12" width="4" height="8" rx="1.5"/>
      <rect x="29" y="12" width="4" height="8" rx="1.5"/>
      <path d="M13 19h22l10 19c0 3-2 4-4 4H7c-2 0-4-1-4-4z"/>
      <rect x="7" y="40" width="5" height="7" rx="2"/>
      <rect x="36" y="40" width="5" height="7" rx="2"/>
      <circle cx="24" cy="30" r="6" fill="#efefef"/>
      <circle cx="24" cy="30" r="3.2"/>
    </svg>
    <div class="phones">
      <div>Spain (+34) 612 480 397</div>
      <div>(USA) +1 (555) 318 2046</div>
    </div>

    <svg class="contact-icon contact-icon--web" viewBox="0 0 45 45" aria-hidden="true">
      <g fill="none" stroke="var(--brand-blue)" stroke-width="4">
        <circle cx="22.5" cy="22.5" r="20"/>
        <ellipse cx="22.5" cy="22.5" rx="9" ry="20"/>
        <line x1="22.5" y1="2.5" x2="22.5" y2="42.5"/>
        <line x1="3" y1="16" x2="42" y2="16"/>
        <line x1="3" y1="29" x2="42" y2="29"/>
      </g>
    </svg>
    <div class="website">www.marlovitality.example</div>

    <div class="footer-band"></div>
  </section>
</main>
</body>
</html>
```